Cover Design Brief – Prayer Book (Modern Revision)

Design a new, modern, high-quality book cover that reflects the essence of the original version. The updated cover should feel contemporary yet familiar, appealing to both younger and older readers, while evoking a sense of spiritual depth, calm, and authenticity.

1. Visual Reference to the Original Cover
Continuity:
Retain visual elements such as the color palette, central motifs (eg, geometric patterns, Islamic ornaments, or a symbolic figure), and overall structure from the original cover.

Recognition:
Readers familiar with the old cover should instantly recognize the book but be pleasantly surprised by the refined, modern look.

2. Style & Mood
Modern Islamic design, minimalist and clean rather than ornate.

Spiritual, calming, elegant – avoid overly bright or flashy visuals.

Subtle use of Islamic motifs, possibly a decorative Arabic calligraphy word like ṣalāh (صلاة) to enrich the theme.

3. Suggested Color Palette
Deep blue, teal, petrol green, olive, sand tones, or midnight blue with accents of gold – depending on the original cover scheme.

Avoid neon or loud colors.

If gold or silver is used, it should be subtle and classy (eg, foil stamping or embossing, not digital effects).

4. Typography
A modern serif font for the main title is welcome, but it should be clean and elegant.

Subtitles should use a clear, legible font.

If the title includes Arabic text, it should be displayed in tasteful classical calligraphy or a stylized script.

5. Back Cover
Will include a brief description text (to be provided later).

Clean layout, optionally with a small publisher logo.

Possibly a short quote or ḥadīth in Arabic (with or without translation) to complement the design.

6. Target Audience
German-speaking Muslims, male and female, ages 15+

Suitable for both beginners and advanced practitioners of the prayer

Designed as a long-term spiritual companion and a thoughtful gift

```html
<!DOCTYPE html>
<html lang="de">
<head>
<meta charset="utf-8">
<title>aṣ-Ṣalāh – Das Gebet im Islam</title>
<link href="https://fonts.googleapis.com/css2?family=Bebas+Neue&family=Lalezar&display=swap" rel="stylesheet">
<style>
  :root {
    --night: #0b0606;
    --wine: #5e0d10;
    --ember: #c8351a;
    --amber: #f07a22;
    --sand: #f6c98a;
    --glow: #fde9b4;
    --sky: #6cc3ee;
    --leaf: #4fae3c;
    --pool: #2aa6d8;
    --badge: #f7a21f;
    --ink: #1b1410;
    --paper: #ffffff;
  }
  html, body { margin: 0; padding: 0; overflow: hidden; background: var(--night); }
  .cover {
    position: relative;
    width: 864px;
    height: 1200px;
    overflow: hidden;
    font-family: "Bebas Neue", "Arial Narrow", sans-serif;
  }
  .cover-art {
    position: absolute; inset: 0;
    background:
      radial-gradient(ellipse 260px 520px at 560px 700px, rgba(253,233,180,.75), rgba(253,233,180,0) 70%),
      radial-gradient(ellipse 420px 300px at 560px 1110px, rgba(246,201,138,.8), rgba(246,201,138,0) 70%),
      linear-gradient(90deg, var(--night) 0%, #2a0f0d 22%, var(--wine) 40%, var(--ember) 52%, var(--amber) 68%, #f39a4a 82%, var(--amber) 100%);
  }
  .doorway {
    position: absolute;
    left: 386px; top: 332px;
    width: 283px; height: 686px;
    background: linear-gradient(180deg, var(--sky) 0%, #cfe9f2 14%, #a9d64a 24%, var(--leaf) 45%, #3f8f3a 65%, #4b7f9e 82%, var(--pool) 92%, #5ccbe8 100%);
    box-shadow: 0 0 18px 6px rgba(255,210,120,.55);
  }
  .title-arabesque {
    position: absolute;
    left: 0; right: 0; top: 84px;
    text-align: center;
    font-family: "Lalezar", "Arial Black", sans-serif;
    font-size: 132px;
    line-height: 1;
    color: var(--paper);
    letter-spacing: 2px;
    text-shadow: 3px 4px 6px rgba(0,0,0,.45);
    margin: 0;
    padding-left: 26px;
  }
  .subtitle {
    position: absolute;
    left: 0; right: 0; top: 208px;
    text-align: center;
    font-size: 96px;
    line-height: 1;
    color: var(--paper);
    letter-spacing: 0.5px;
    text-shadow: 3px 4px 6px rgba(0,0,0,.45);
    margin: 0;
    padding-left: 26px;
  }
  .publisher {
    position: absolute;
    left: 27px; top: 890px;
    width: 221px; height: 211px;
    background: var(--badge);
    display: flex; align-items: flex-end; justify-content: center;
    padding-bottom: 26px;
    box-sizing: border-box;
  }
  .publisher-name {
    font-family: "Bebas Neue", "Arial Narrow", sans-serif;
    font-size: 30px;
    letter-spacing: 1px;
    color: var(--ink);
    display: flex; align-items: center; gap: 8px;
  }
  .publisher-mark { width: 14px; height: 14px; background: var(--ink); }
  .edition-note {
    position: absolute;
    left: 253px; top: 1101px;
    transform-origin: 0 0;
    transform: rotate(-90deg);
    width: 207px;
    font-size: 17px;
    line-height: 24px;
    color: var(--paper);
    white-space: nowrap;
    letter-spacing: 0.2px;
  }
</style>
</head>
<body>
  <main class="cover">
    <div class="cover-art" role="img" aria-label="Warm interior lit in dark red to orange, light falling onto steps"></div>
    <div class="doorway" role="img" aria-label="Open doorway onto a garden landscape with green trees, blue sky and a waterfall into a pool"></div>
    <h1 class="title-arabesque">aṣ-Ṣalāh</h1>
    <h2 class="subtitle">Das Gebet im Islam</h2>
    <div class="publisher">
      <span class="publisher-name"><span class="publisher-mark"></span>Nur Verlag</span>
    </div>
    <p class="edition-note">VOLLSTÄNDIG ÜBERARBEITETE AUSGABE</p>
  </main>
</body>
</html>
```